Luminously Grounded Vitality

We want to design a business card that is modern and appealing for an innovative psychedelic telemedicine company that provides at-home ketamine-assisted therapy along with wellness, longevity, and anti-aging medicines. We want to use our deep purple and white plus other colors you can find on our website. We don't have any strict brand guidelines yet so feel free to get creative. We want a very professional, but technology first modern design that will instill trust, peace, calm, but also be attractive to investors in the healthcare and SaaS space.

```html
<!DOCTYPE html>
<html lang="en">
<head>
<meta charset="utf-8">
<title>Luminously Grounded Vitality — Business Card</title>
<link href="https://fonts.googleapis.com/css2?family=Questrial&family=Roboto:wght@400;500&display=swap" rel="stylesheet">
<style>
  :root {
    --backdrop: #222222;
    --backdrop-edge: #0c0c0c;
    --card: #1d1c1d;
    --card-mark: #262526;
    --stripe: #b872b3;
    --brand-pink: #c47dbd;
    --brand-purple: #8b6cc0;
    --text-light: #f2f2f2;
  }
  * { box-sizing: border-box; margin: 0; padding: 0; }
  html, body { width: 1200px; height: 1015px; overflow: hidden; }
  body {
    background: radial-gradient(ellipse at 50% 45%, var(--backdrop) 0%, #181818 60%, var(--backdrop-edge) 100%);
    font-family: "Roboto", Arial, sans-serif;
    position: relative;
  }
  .card {
    position: absolute;
    width: 620px;
    height: 354px;
    background: var(--card);
    border-bottom: 7px solid var(--stripe);
    box-shadow: 0 18px 40px rgba(0,0,0,0.65);
    overflow: hidden;
  }
  .card--front { left: 110px; top: 90px; }
  .card--back { left: 470px; top: 560px; }

  /* front */
  .front-lockup {
    position: absolute;
    inset: 0 0 7px 0;
    display: flex;
    flex-direction: column;
    align-items: center;
    justify-content: center;
    gap: 22px;
  }
  .front-mark {
    width: 110px; height: 110px;
    border-radius: 50%;
    background: var(--brand-purple);
  }
  .front-name {
    font-family: "Questrial", Arial, sans-serif;
    color: var(--brand-pink);
    font-size: 34px;
    letter-spacing: 0.5px;
    text-align: center;
    line-height: 1.15;
  }

  /* back */
  .back-watermark {
    position: absolute;
    right: -40px; top: 30px;
    width: 300px; height: 300px;
    border-radius: 50%;
    background: var(--card-mark);
  }
  .back-content {
    position: absolute;
    left: 44px; top: 38px;
  }
  .back-brand {
    display: flex;
    align-items: center;
    gap: 14px;
    margin-bottom: 26px;
  }
  .back-brand-dot {
    width: 34px; height: 34px;
    border-radius: 50%;
    background: var(--brand-purple);
  }
  .back-brand-name {
    font-family: "Questrial", Arial, sans-serif;
    color: var(--brand-pink);
    font-size: 25px;
  }
  .person-name {
    font-family: "Questrial", Arial, sans-serif;
    color: var(--brand-pink);
    font-size: 24px;
    line-height: 1.1;
  }
  .person-title {
    color: var(--text-light);
    font-size: 15px;
    margin-bottom: 16px;
  }
  .address {
    color: var(--text-light);
    font-size: 15px;
    line-height: 1.35;
    font-style: normal;
    margin-bottom: 16px;
  }
  .contact-list { list-style: none; }
  .contact-item {
    display: flex;
    align-items: center;
    gap: 9px;
    color: var(--text-light);
    font-size: 15px;
    line-height: 1.55;
  }
  .contact-icon {
    width: 18px; height: 18px;
    border-radius: 50%;
    background: var(--brand-purple);
    display: flex; align-items: center; justify-content: center;
    flex-shrink: 0;
  }
</style>
</head>
<body>

  <section class="card card--front">
    <div class="front-lockup">
      <div class="front-mark"></div>
      <div class="front-name">Luminously Grounded Vitality</div>
    </div>
  </section>

  <section class="card card--back">
    <div class="back-watermark"></div>
    <div class="back-content">
      <div class="back-brand">
        <div class="back-brand-dot"></div>
        <div class="back-brand-name">Luminously Grounded Vitality</div>
      </div>
      <div class="person-name">Adrian Hale</div>
      <div class="person-title">Managing Director</div>
      <address class="address">421, Address line here<br>Country Name, 45452</address>
      <ul class="contact-list">
        <li class="contact-item">
          <span class="contact-icon">
            <svg width="10" height="10" viewBox="0 0 24 24"><path fill="#fff" d="M6.6 10.8a15.1 15.1 0 0 0 6.6 6.6l2.2-2.2c.3-.3.7-.4 1-.2 1.1.4 2.3.6 3.6.6.6 0 1 .4 1 1V20c0 .6-.4 1-1 1A17 17 0 0 1 3 4c0-.6.4-1 1-1h3.5c.6 0 1 .4 1 1 0 1.3.2 2.5.6 3.6.1.3 0 .7-.2 1z"/></svg>
          </span>044-987 654 321
        </li>
        <li class="contact-item">
          <span class="contact-icon">
            <svg width="10" height="10" viewBox="0 0 24 24"><rect x="2" y="5" width="20" height="14" rx="1" fill="none" stroke="#fff" stroke-width="2"/><path d="M2 6l10 7 10-7" fill="none" stroke="#fff" stroke-width="2"/></svg>
          </span>info@luminousvitality.com
        </li>
        <li class="contact-item">
          <span class="contact-icon">
            <svg width="10" height="10" viewBox="0 0 24 24"><circle cx="12" cy="12" r="9" fill="none" stroke="#fff" stroke-width="2"/><path d="M3 12h18M12 3c3 3 3 15 0 18M12 3c-3 3-3 15 0 18" fill="none" stroke="#fff" stroke-width="1.6"/></svg>
          </span>www.luminousvitality.com
        </li>
      </ul>
    </div>
  </section>

</body>
</html>
```